Business Card & Email Signature Design || Upmarket + Luxury

Riverlume Honey, a New Zealand Manuka Honey company needs a Business Card & Email Signature design.

Our logo's are attached in Gold & Black versions, feel free to be creative with how you use the logo and it's patterns in your design.

Style:
- Looking for an Elegant, Luxurious, Upmarket feel.
- Black/Matte Black Card, Gold Foil, UV Embossing

Information to Add:

- Logo
- Company Name: Riverlume Honey
- Name: Mattias Brovell
- Title: Creative Director
- Phone: +64 2919 58 617
- Email: mattias@riverlumehoney.example
- Website: www.riverlumehoney.example

- Socials: ***For email Signature Only***
- Facebook: https://www.facebook.com/riverlumehoney/
- Instagram: https://www.instagram.com/riverlumehoney/

Target Market(s)

Asia/Europe Luxury, Upmarket

Contact Information for Business Card

- Logo
- Name: Mattias Brovell
- Phone: +64 2919 58 617

Font styles to use
Other font styles liked:
• Champagne & Limousines (Attached)

Requirements
Must have
• Business Card & Email Signature Design.

Looking for a Sleek, Luxury, Upmarket Design.

```html
<!DOCTYPE html>
<html lang="en">
<head>
<meta charset="utf-8">
<title>Riverlume Honey — Business Card</title>
<link rel="stylesheet" href="https://fonts.googleapis.com/css2?family=Mulish:wght@500;600;800&display=swap">
<style>
  :root {
    --backdrop: #d6d6d4;
    --card-black: #262626;
    --foil-gold: #c9a861;
    --shadow: rgba(0, 0, 0, 0.28);
  }
  * { margin: 0; padding: 0; box-sizing: border-box; }
  html, body {
    width: 1200px;
    height: 747px;
    overflow: hidden;
    background: var(--backdrop);
  }
  .canvas {
    position: relative;
    width: 1200px;
    height: 747px;
  }
  .business-card {
    position: absolute;
    left: 395px;
    top: 38px;
    width: 410px;
    height: 671px;
    background: var(--card-black);
    box-shadow: 0 14px 30px var(--shadow);
    font-family: "Mulish", sans-serif;
    color: var(--foil-gold);
  }
  .brand-mark {
    position: absolute;
    top: 42px;
    right: 36px;
    display: flex;
    align-items: center;
    gap: 10px;
    font-size: 15px;
    font-weight: 600;
    letter-spacing: 0.14em;
    text-transform: uppercase;
  }
  .brand-mark .dot {
    width: 14px;
    height: 14px;
    border: 1.5px solid var(--foil-gold);
    border-radius: 50%;
  }
  .identity {
    position: absolute;
    left: 40px;
    top: 292px;
  }
  .person-name {
    font-size: 35px;
    font-weight: 800;
    letter-spacing: 0.03em;
    text-transform: uppercase;
    line-height: 1;
    white-space: nowrap;
  }
  .job-title {
    margin-top: 6px;
    font-size: 21px;
    font-weight: 600;
    letter-spacing: 0.03em;
  }
  .contact-list {
    position: absolute;
    left: 40px;
    top: 396px;
    list-style: none;
  }
  .contact-list li {
    display: flex;
    align-items: center;
    gap: 14px;
    font-size: 17px;
    font-weight: 600;
    letter-spacing: 0.02em;
    line-height: 29px;
    white-space: nowrap;
  }
  .contact-list li::before {
    content: "";
    width: 13px;
    height: 13px;
    background: var(--foil-gold);
    flex: none;
  }
  .company-address {
    position: absolute;
    left: 40px;
    bottom: 60px;
    font-style: normal;
    font-size: 20px;
    font-weight: 500;
    line-height: 30px;
    letter-spacing: 0.02em;
  }
  .company-address .company-name {
    text-transform: uppercase;
    font-size: 21px;
  }
</style>
</head>
<body>
  <main class="canvas">
    <article class="business-card">
      <div class="brand-mark">
        <span class="dot"></span>
        <span class="brand-name">Riverlume Honey</span>
      </div>

      <header class="identity">
        <h1 class="person-name">Mattias Brovell</h1>
        <p class="job-title">Creative Director</p>
      </header>

      <ul class="contact-list">
        <li class="phone">+64 2919 58 617</li>
        <li class="email">mattias@riverlumehoney.example</li>
        <li class="website">www.riverlumehoney.example</li>
      </ul>

      <address class="company-address">
        <div class="company-name">Riverlume Honey</div>
        <div>Address line one and door no</div>
        <div>Address line two and pincode</div>
      </address>
    </article>
  </main>
</body>
</html>
```